Hairdressing Salon called; Tressel Studio. Style Is Us

Tressel Studio
We Love Hair
418 Wexbury Lane Hollin Park
4839172
Business card not to fussy.
I would like it to be a Black background with White and/or Grey lettering.

I really like the business card attached, so if the front looked like this I would be really happy, but would also like my address and phone number on the front.

On the back I would like two options of
1: reward card; buy any Haircare product over $20 on any visit and on the tenth product receive a complimentry Treatment and
2: appointment times and date

Business

Tressel Studio
We Love Hair
4839172
418 Wexbury Lane, Hollin Park
This must all be included on the front of the card

Serif
Decorative
Script

1b1b1b
757575
ffffff

Must have
• My phone number and address
Should not have
• Pictures on the front

```html
<!DOCTYPE html>
<html lang="en">
<head>
<meta charset="utf-8">
<title>Tressel Studio – Business Card Front</title>
<link rel="stylesheet" href="https://fonts.googleapis.com/css2?family=Poiret+One&family=Marcellus+SC&family=Parisienne&display=swap">
<style>
  :root {
    --ink-black: #1b1b1b;
    --band-black: #161616;
    --side-charcoal: #2c3031;
    --side-edge: #1f2223;
    --ornament-grey: #757575;
    --text-white: #ffffff;
  }
  html, body {
    margin: 0;
    padding: 0;
    width: 1200px;
    height: 698px;
    overflow: hidden;
    background: var(--ink-black);
  }
  .card {
    position: relative;
    width: 1200px;
    height: 698px;
    overflow: hidden;
    background: var(--ink-black);
  }
  .damask-panel {
    position: absolute;
    top: 0;
    width: 312px;
    height: 698px;
  }
  .damask-panel--left {
    left: 0;
    background: linear-gradient(90deg, var(--side-edge) 0%, var(--side-charcoal) 100%);
  }
  .damask-panel--right {
    right: 0;
    background: linear-gradient(270deg, var(--side-edge) 0%, var(--side-charcoal) 100%);
  }
  .center-band {
    position: absolute;
    top: 0;
    left: 312px;
    width: 576px;
    height: 698px;
    background: linear-gradient(180deg, #1e1e1e 0%, var(--band-black) 55%, #101010 100%);
  }
  .brand-circle {
    position: absolute;
    left: 537px;
    top: 62px;
  }
  .scroll-ornament {
    position: absolute;
    left: 340px;
    width: 520px;
    border-radius: 40px;
    background: radial-gradient(ellipse at center, rgba(117,117,117,0.35) 0%, rgba(117,117,117,0.12) 60%, rgba(117,117,117,0) 100%);
  }
  .scroll-ornament--top { top: 200px; height: 78px; }
  .scroll-ornament--bottom { top: 374px; height: 74px; }
  .salon-name {
    position: absolute;
    left: 0;
    top: 300px;
    width: 1200px;
    margin: 0;
    text-align: center;
    font-family: "Poiret One", sans-serif;
    font-weight: 400;
    font-size: 56px;
    line-height: 70px;
    letter-spacing: 1px;
    color: var(--text-white);
    text-transform: uppercase;
  }
  .contact {
    position: absolute;
    left: 0;
    top: 470px;
    width: 1200px;
    margin: 0;
    text-align: center;
    font-family: "Marcellus SC", serif;
    font-size: 30px;
    line-height: 36px;
    color: var(--text-white);
    font-style: normal;
  }
  .contact span { display: block; }
  .tagline {
    position: absolute;
    left: 0;
    top: 586px;
    width: 1200px;
    margin: 0;
    text-align: center;
    font-family: "Parisienne", cursive;
    font-size: 56px;
    line-height: 80px;
    color: var(--text-white);
  }
</style>
</head>
<body>
  <main class="card">
    <div class="damask-panel damask-panel--left" role="img" aria-label="Dark grey damask wallpaper pattern"></div>
    <div class="damask-panel damask-panel--right" role="img" aria-label="Dark grey damask wallpaper pattern"></div>
    <div class="center-band" role="img" aria-label="Black band with faint damask pattern"></div>

    <svg class="brand-circle" width="126" height="126" viewBox="0 0 126 126" aria-hidden="true">
      <circle cx="63" cy="63" r="58" fill="none" stroke="var(--text-white)" stroke-width="8"/>
    </svg>

    <div class="scroll-ornament scroll-ornament--top" role="img" aria-label="Ornamental scrollwork flourish above the salon name"></div>
    <h1 class="salon-name">Tressel Studio</h1>
    <div class="scroll-ornament scroll-ornament--bottom" role="img" aria-label="Ornamental scrollwork flourish below the salon name"></div>

    <address class="contact">
      <span class="contact__address">418 Wexbury Lane Hollin Park</span>
      <span class="contact__phone">4839172</span>
    </address>

    <p class="tagline">We love hair</p>
  </main>
</body>
</html>
```